Trifold Brochure

This is relatively easy. We already have a trifold made we simply want to update the LOOK to look more like our current website. All content would stay the same the only thing that would change would be the fonts, colors and background images to match the current website.

I have attached a word doc of the old trifold brochure. We would want the content to remain on the same pages of the trifold. Again all you are doing is updating the font, logo, colors and any background images. Please comment with any questions.

This is a 5 day project!

Requirements
Must have
• Logo, colors and fonts to match our current website.
http://www.brackenfieldworks.example/

```html
<!DOCTYPE html>
<html lang="en">
<head>
<meta charset="utf-8">
<title>Brackenfield Structural Works – Trifold Brochure</title>
<link href="https://fonts.googleapis.com/css2?family=Montserrat:wght@600;700&family=Questrial&display=swap" rel="stylesheet">
<style>
:root{
  --green-dark:#4f6b2b;
  --green-deep:#3e5720;
  --green-head:#4a6828;
  --green-band:#c8dea4;
  --green-soft:#dcebc3;
  --ink:#2b2b2b;
  --text:#444;
  --card-top:#ffffff;
  --card-bottom:#ececec;
  --stage:#e6e2dc;
}
*{box-sizing:border-box;margin:0;padding:0}
html,body{width:1200px;height:946px;overflow:hidden;background:var(--stage)}
body{position:relative;font-family:"Questrial",sans-serif;color:var(--text)}
.brochure{position:absolute;left:48px;top:47px;width:1104px;height:853px;display:flex;box-shadow:0 2px 8px rgba(0,0,0,.25)}
.panel{position:relative;width:368px;height:100%;overflow:hidden;
  background:radial-gradient(circle at 30% 20%,#5b7832 0%,var(--green-dark) 55%,var(--green-deep) 100%)}
.panel + .panel{border-left:1px solid rgba(255,255,255,.35)}
.pattern{position:absolute;inset:0}
.band{position:absolute;left:0;right:0;top:639px;height:196px;background:linear-gradient(180deg,var(--green-soft),var(--green-band))}
.strip{position:absolute;left:0;right:0;bottom:0;height:18px;background:var(--green-dark)}
.panel-title{position:absolute;top:26px;left:0;right:0;text-align:center;color:#fff;font-family:"Montserrat",sans-serif;font-weight:700;font-size:20px}
.card{position:absolute;top:59px;left:19px;width:331px;height:580px;border-radius:12px 12px 0 0;
  background:linear-gradient(180deg,var(--card-top) 40%,var(--card-bottom));padding:16px 15px 0}
.card p{font-size:12.4px;line-height:15.1px;text-align:justify;margin-bottom:15px}
.notes p{font-style:italic}
.notes .lead{font-weight:600;margin:6px 0 15px}
.mark{position:absolute;background:var(--green-soft);border:3px solid #f1f6e7;outline:1px solid #9fb77d;
  display:flex;align-items:center;justify-content:center;font-family:"Montserrat",sans-serif;font-weight:700;color:var(--green-dark)}
.brand-name{position:absolute;font-family:"Montserrat",sans-serif;font-weight:700;color:var(--ink)}
.phone-big{position:absolute;left:76px;top:781px;font-family:"Montserrat",sans-serif;font-weight:700;font-size:29px;color:var(--ink);display:flex;align-items:center;gap:4px}
.web-small{position:absolute;left:78px;top:818px;font-size:13.5px;color:var(--ink);display:flex;align-items:center;gap:5px}
.contact{position:absolute;left:80px;font-size:12.5px;line-height:15.5px;color:var(--ink);display:flex;gap:6px}
.contact svg{flex:none;margin-top:2px}
.hero-card{position:absolute;left:22px;top:321px;width:331px;height:318px;border-radius:12px 12px 0 0;
  background:linear-gradient(180deg,var(--card-top) 50%,var(--card-bottom));text-align:center;padding-top:22px}
.hero-card h1{font-family:"Montserrat",sans-serif;font-weight:700;font-size:31px;line-height:40px;color:var(--green-head);letter-spacing:.5px}
.tagline{position:absolute;top:651px;left:0;right:0;text-align:center;font-size:21.5px;line-height:28px;color:var(--ink)}
.cover-name{position:absolute;top:213px;left:0;right:0;text-align:center;color:#fff;font-family:"Montserrat",sans-serif;font-weight:700;font-size:23px;line-height:30px}
</style>
</head>
<body>
<main class="brochure">

  <section class="panel panel-inside">
    <div class="pattern" role="img" aria-label="Woven line pattern in green tones"></div>
    <h2 class="panel-title">WHO WE ARE</h2>
    <div class="card">
      <p>Following the devastation of Hurricane Sandy, countless homes along the Northeast Coastline were dislodged from their piling foundations. Some of the pilings were completely destroyed while others subsided. Brackenfield Structural Works, LLC (BSW) was established by a team of Engineers, Designers and Material Specialists that witnessed the destructive aftermath personally. This highly skilled team provided engineering services to home owners along the coast at the initial stage of the aftermath recovery efforts. During this time, the BSW team identified a need for an improved solution.</p>
      <p>Traditional options available on the market presented problems for the recovery of homes on pilings that needed to be repaired or raised. Options provided to homeowners had drawbacks. The traditional method includes lifting and moving the home away from the pilings, then drive new pilings, and then move the home back. This alternative presented several problems, such as cost and where to place the house during the reinstallation of the pilings. Simply put there is no room for this option in most cases.</p>
      <p>As a result, BSW developed a system which allows the house to be raised without actually moving the home, the Collars installed, and the house reset on the Collars without the expense of moving the house or driving new pilings. This option can be installed in a matter of days with limited space and at a lower construction cost. Please see our technical brief for a review of your options and how our system compares to other methods.</p>
    </div>
    <div class="band" role="img" aria-label="Light green band with line pattern"></div>
    <div class="strip"></div>
    <div class="mark" style="left:64px;top:677px;width:78px;height:78px;font-size:20px">BSW</div>
    <div class="brand-name" style="left:168px;top:684px;font-size:21px;line-height:26px">BRACKENFIELD<br>STRUCTURAL<br>WORKS, LLC</div>
    <div class="phone-big">
      <svg width="28" height="28" viewBox="0 0 24 24" aria-hidden="true"><circle cx="12" cy="12" r="10.5" fill="none" stroke="#2b2b2b" stroke-width="1.6"/><path d="M8.5 6.5c-1.5 1-1.2 4.5 1.8 7.6s6.3 3.5 7.2 2.1l-2.2-2.2-1.6 1c-1.3-.6-3.1-2.4-3.7-3.7l1-1.6z" fill="#2b2b2b"/></svg>
      555.014.2170
    </div>
    <div class="web-small">
      <svg width="13" height="13" viewBox="0 0 16 16" aria-hidden="true"><circle cx="8" cy="8" r="7" fill="none" stroke="#2b2b2b" stroke-width="1.2"/><ellipse cx="8" cy="8" rx="3" ry="7" fill="none" stroke="#2b2b2b"/><path d="M1 8h14M2.5 4.5h11M2.5 11.5h11" stroke="#2b2b2b"/></svg>
      www.brackenfieldworks.example
    </div>
  </section>

  <section class="panel panel-back">
    <div class="pattern" role="img" aria-label="Woven line pattern in green tones"></div>
    <h2 class="panel-title" style="font-weight:600">Designer’s Corner:</h2>
    <div class="card notes" style="left:18px">
      <p class="lead">Notes to Design Professionals:</p>
      <p>We have a staff Engineer who can assist you with developing permit plans for submission for approval under Section 104.11 of the IRC. We can provide you with standard details in ACAD format with appropriate construction notes and detailed product specification for use in construction documents.</p>
      <p>When designing using our systems, be sure to understand that our system is simply an extension of the piling, and as such, standard lateral supporting must be considered.</p>
      <p>An inspection of each piling is required by the professional to ensure that the piling is free from alignment deflection of greater than 6 degrees, free from dry rot, damage or other defect.</p>
      <p>Our system can be installed below grade, if there is dry rot on the exposed surface of the pile, dig down into the sand, it is likely the piling below the sand and/or the water table is structurally sound. The BSW system can be used as a splice to remove failed sections of pilings and install new sections.</p>
    </div>
    <div class="band" role="img" aria-label="Light green band with line pattern"></div>
    <div class="strip"></div>
    <div class="mark" style="left:149px;top:572px;width:74px;height:74px;font-size:19px">BSW</div>
    <div class="brand-name" style="left:0;right:0;top:670px;text-align:center;font-size:14.5px">BRACKENFIELD STRUCTURAL WORKS, LLC</div>
    <div class="contact" style="top:707px">
      <svg width="10" height="13" viewBox="0 0 10 14" aria-hidden="true"><path d="M5 0a5 5 0 0 0-5 5c0 3.5 5 9 5 9s5-5.5 5-9a5 5 0 0 0-5-5zm0 7a2 2 0 1 1 0-4 2 2 0 0 1 0 4z" fill="#2b2b2b"/></svg>
      <span>PO Box 4120, Harlow Valley,<br>PA 10000-0090</span>
    </div>
    <div class="contact" style="top:751px">
      <svg width="12" height="26" viewBox="0 0 12 26" aria-hidden="true"><path d="M1 5c0-2 10-2 10 0l-2 1-1-1H4L3 6zM2 7h8v3H2z" fill="#2b2b2b"/><path d="M2 17h8v6H2zM3 15h6v2H3z" fill="none" stroke="#2b2b2b"/></svg>
      <span>555.014.2170<br>555.014.1491</span>
    </div>
    <div class="contact" style="top:797px">
      <svg width="12" height="26" viewBox="0 0 12 26" aria-hidden="true"><rect x=".5" y="2.5" width="11" height="8" fill="none" stroke="#2b2b2b"/><path d="M.5 2.5l5.5 4.5 5.5-4.5" fill="none" stroke="#2b2b2b"/><circle cx="6" cy="20" r="5" fill="none" stroke="#2b2b2b"/><path d="M1 20h10M6 15v10" stroke="#2b2b2b" stroke-width=".8"/></svg>
      <span>sales@brackenfieldworks.example<br>www.brackenfieldworks.example</span>
    </div>
  </section>

  <section class="panel panel-cover">
    <div class="pattern" role="img" aria-label="Woven line pattern in green tones"></div>
    <div class="mark" style="left:111px;top:55px;width:146px;height:146px;font-size:34px">BSW</div>
    <div class="cover-name">BRACKENFIELD<br>STRUCTURAL<br>WORKS, LLC</div>
    <div class="hero-card">
      <h1>REBUILD<br>SAFER,<br>STRONGER,<br>BETTER,<br>AND BUILD<br>NEW LASTING<br>MEMORIES</h1>
    </div>
    <div class="band" role="img" aria-label="Light green band with line pattern"></div>
    <div class="strip"></div>
    <p class="tagline">We provide piling<br>repair systems to allow for<br>cost effective reconstruction<br>and modifications to<br>structures on pilings</p>
  </section>

</main>
</body>
</html>
```